Coffee Cocktails Recipe Flips cards

create (12) recipe cards that illustrate the finished beverage, with its description, ingredients, and instructions. each card should be 5"x7" and styled to incorporate brand theme and the cultural elements of the beverage. cards will be used for stuffers in shipments of product, used by bartenders, and digitally shared. Present each drink in glassware that embodies the spirit of the culture it represents, garnishing with flair and a nod to the exotic origins, creating a multisensory experience that'll transport the drinker to distant lands with just one indulgent sip.
The presentation of each drink should reflect the cultural fusion aesthetically, using suggested glassware and garnishes to bring the exotic themes to life. Enjoy crafting these drinks and take your guests on a flavorful voyage around the world with each sip!

Target Market(s)

Consumers and Bars and Restaurants

Industry/Entity Type

coffee and adult beverages

Colors

Designer to choose colors to be used in the design.

Requirements
Must have
• brand alignment, styled to reflect the uniqueness of each recipe
Should not have
• appropriate glassware, garnishments, and images of raw ingredients

```html
<!DOCTYPE html>
<html lang="en">
<head>
<meta charset="utf-8">
<title>Rise &amp; Roast — Coffee Recipe Cards</title>
<link href="https://fonts.googleapis.com/css2?family=Allura&family=Roboto+Condensed:wght@400;700&display=swap" rel="stylesheet">
<style>
  :root{
    --page:#e6e6e6;
    --navy:#1b2836;
    --deep:#223846;
    --teal:#5ea5a8;
    --mint:#6cc08a;
    --white:#ffffff;
    --text:#e9f1f1;
    --photo-warm:#8a6a4e;
    --photo-dark:#2a2522;
  }
  *{box-sizing:border-box;margin:0;padding:0}
  html,body{width:1200px;height:1124px;overflow:hidden;background:var(--page)}
  body{position:relative;font-family:"Roboto Condensed",Arial,sans-serif}
  .card{position:absolute;width:345px;height:483px;overflow:hidden;
    background:linear-gradient(205deg,var(--teal) 0%,#3f7a83 30%,var(--deep) 62%,var(--navy) 100%)}
  .card--1{left:68px;top:69px}.card--2{left:429px;top:69px}.card--3{left:787px;top:69px}
  .card--4{left:68px;top:572px}.card--5{left:429px;top:572px}.card--6{left:787px;top:572px}
  .card__art{position:absolute;inset:0;width:345px;height:483px}
  .title{position:absolute;left:0;top:0;width:345px;height:260px;pointer-events:none}
  .title span{position:absolute;white-space:nowrap;font-family:"Allura",cursive;font-size:50px;line-height:1;
    color:var(--mint);-webkit-text-stroke:0.6px var(--navy)}
  .desc{position:absolute;font-size:7.6px;line-height:9.9px;color:var(--text);font-weight:400}
  .recipe{position:absolute;width:180px;color:var(--white)}
  .recipe h3{font-size:8.4px;letter-spacing:3.2px;color:var(--mint);font-weight:400;margin-bottom:4px}
  .recipe ul,.recipe ol{list-style:none;font-size:7.5px;line-height:10.2px;font-weight:700}
  .recipe ul li{position:relative;padding-left:9px}
  .recipe ul li::before{content:"";position:absolute;left:1px;top:4px;width:3px;height:3px;border-radius:50%;background:var(--mint)}
  .recipe ol li{display:flex;gap:5px}
  .recipe ol li b{color:var(--mint);font-weight:400;min-width:6px}
  .recipe hr{border:0;border-top:1px solid #c9d6d8;width:168px;margin:7px 0 8px}
  .logo{position:absolute;left:19px;top:410px;display:flex;flex-direction:column;align-items:flex-start;gap:4px}
  .logo__dot{width:22px;height:22px;border-radius:50%;background:var(--mint);margin-left:14px}
  .logo__name{font-size:17px;line-height:15px;font-weight:700;color:var(--navy)}
</style>
</head>
<body>

<!-- Card 1 -->
<article class="card card--1">
  <svg class="card__art" viewBox="0 0 345 483">
    <path d="M345 300C315 305 310 345 330 370C345 395 325 440 310 483H345Z" fill="var(--mint)"/>
    <path d="M0 0H305C335 60 340 205 303 245C272 278 230 262 198 232C168 202 138 168 80 163C40 160 15 168 0 176Z" fill="none" stroke="var(--mint)" stroke-width="5"/>
    <path role="img" aria-label="Photo of an iced mocha with whipped cream and chocolate shavings in an autumn park" d="M0 0H300C330 60 333 200 298 238C268 270 230 256 200 228C170 200 140 162 80 157C40 154 15 160 0 168Z" fill="url(#g1)"/>
    <ellipse cx="36" cy="488" rx="104" ry="108" fill="none" stroke="var(--mint)" stroke-width="4"/>
    <ellipse cx="28" cy="488" rx="100" ry="106" fill="var(--white)"/>
    <defs><linearGradient id="g1" x1="0" y1="0" x2="1" y2="1"><stop offset="0" stop-color="#7a8a4a"/><stop offset=".5" stop-color="#8d6d55"/><stop offset="1" stop-color="#6a3d22"/></linearGradient></defs>
  </svg>
  <div class="title"><span style="left:19px;top:94px">Café Mocha</span><span style="left:168px;top:142px">Bliss</span></div>
  <p class="desc" style="left:19px;top:187px;width:98px">Indulge in the balance of bittersweet espresso entwined with rich chocolate syrup to enjoy the luxe texture of the Café Mocha Bliss. Gently pour the espresso into your favorite mug, caress it with the velvety touch of chocolate, and crown the mix with steamed milk as soft as clouds. End with a swirl of whipped cream, graced with a sprinkling of chocolate shavings or a delicate dusting of cocoa powder—your canvas of comfort.</p>
  <div class="recipe" style="left:152px;top:281px">
    <h3>INGREDIENTS:</h3>
    <ul><li>5g R&amp;R Classic Black Coffee</li><li>8oz hot water</li><li>2 tablespoons chocolate syrup</li><li>Steamed milk</li><li>Whipped cream</li><li>Chocolate shavings for garnish</li></ul>
    <hr>
    <h3>INSTRUCTIONS:</h3>
    <ol><li><b>1.</b><span>Mix 8oz of hot water with one packet R&amp;R Classic Black Instant Coffee, mix well until powder is fully dissolved.</span></li><li><b>2.</b><span>Pour the Coffee into a mug.</span></li><li><b>3.</b><span>Stir in the chocolate syrup until well combined.</span></li><li><b>4.</b><span>Top with steamed milk.</span></li><li><b>5.</b><span>Add a generous dollop of whipped cream.</span></li><li><b>6.</b><span>Garnish with chocolate shavings.</span></li></ol>
  </div>
  <div class="logo"><span class="logo__dot"></span><span class="logo__name">RISE &amp;<br>ROAST</span></div>
</article>

<!-- Card 2 -->
<article class="card card--2">
  <svg class="card__art" viewBox="0 0 345 483">
    <path d="M345 300C315 305 310 345 330 370C345 395 325 440 310 483H345Z" fill="var(--mint)"/>
    <path d="M0 0H170C212 70 222 240 203 300C192 324 120 326 0 322Z" fill="none" stroke="var(--mint)" stroke-width="5"/>
    <path role="img" aria-label="Photo of an iced vanilla latte with whipped cream beside small pumpkins and coffee beans" d="M0 0H168C208 70 216 236 198 294C188 316 120 318 0 315Z" fill="url(#g2)"/>
    <ellipse cx="36" cy="488" rx="104" ry="108" fill="none" stroke="var(--mint)" stroke-width="4"/>
    <ellipse cx="28" cy="488" rx="100" ry="106" fill="var(--white)"/>
    <defs><linearGradient id="g2" x1="0" y1="0" x2="1" y2="1"><stop offset="0" stop-color="#1e2024"/><stop offset=".5" stop-color="#a8703a"/><stop offset="1" stop-color="#3a2a22"/></linearGradient></defs>
  </svg>
  <div class="title"><span style="left:27px;top:112px">Vanilla</span><span style="left:27px;top:163px">Bean Dream</span></div>
  <p class="desc" style="left:233px;top:20px;width:97px">Picture a serene autumn afternoon as you sip on the smooth Vanilla Bean Dream. Begin by mixing robust cold brew coffee with the sweet whispers of vanilla syrup. Lull the mix into a tall glass over generous cubes of ice and drape it with a splash of milk. A vanilla pod or a subtle dash of ground vanilla makes for the quintessential garnish to this dreamy concoction.</p>
  <div class="recipe" style="left:152px;top:292px">
    <h3>INGREDIENTS:</h3>
    <ul><li>5g R&amp;R Classic Black Coffee</li><li>8oz hot water</li><li>2 tablespoons vanilla syrup</li><li>Milk</li><li>Ice cubes</li><li>A vanilla pod for garnish</li></ul>
    <hr>
    <h3>INSTRUCTIONS:</h3>
    <ol><li><b>1.</b><span>Mix 8oz of hot water with one packet R&amp;R Classic Black Instant Coffee, mix well until powder is fully dissolved.</span></li><li><b>2.</b><span>Fill a glass with ice cubes.</span></li><li><b>3.</b><span>Combine coffee and vanilla syrup.</span></li><li><b>4.</b><span>Add milk to taste and stir well.</span></li><li><b>5.</b><span>Garnish with a vanilla pod.</span></li></ol>
  </div>
  <div class="logo"><span class="logo__dot"></span><span class="logo__name">RISE &amp;<br>ROAST</span></div>
</article>

<!-- Card 3 -->
<article class="card card--3">
  <svg class="card__art" viewBox="0 0 345 483">
    <path d="M345 300C315 305 310 345 330 370C345 395 325 440 310 483H345Z" fill="var(--mint)"/>
    <path d="M0 112C30 105 55 125 50 150C45 175 20 190 0 186Z" fill="var(--mint)"/>
    <path d="M104 142A118 118 0 0 0 330 190" fill="none" stroke="var(--mint)" stroke-width="6"/>
    <circle role="img" aria-label="Photo of a cinnamon latte dusted with spice, cinnamon sticks resting on the saucer" cx="218" cy="138" r="116" fill="url(#g3)"/>
    <ellipse cx="36" cy="488" rx="104" ry="108" fill="none" stroke="var(--mint)" stroke-width="4"/>
    <ellipse cx="28" cy="488" rx="100" ry="106" fill="var(--white)"/>
    <defs><radialGradient id="g3"><stop offset="0" stop-color="#b48a6a"/><stop offset=".55" stop-color="#e8e2dc"/><stop offset="1" stop-color="#cfcac6"/></radialGradient></defs>
  </svg>
  <div class="title"><span style="left:34px;top:30px">Cinnamon</span><span style="left:34px;top:85px">Swirl Latte</span></div>
  <p class="desc" style="left:20px;top:218px;width:100px">Warm your spirit with a Cinnamon Swirl Latte, reminiscent of the spice markets in an exotic locale. Brew your espresso with care, introducing it to a dance with the golden cinnamon syrup. As the duo unites, lay a blanket of frothed milk atop and crown with a confetti of cinnamon powder. You may choose to lean a cinnamon stick as a companion for this warm, spicy elixir.</p>
  <div class="recipe" style="left:152px;top:292px">
    <h3>INGREDIENTS:</h3>
    <ul><li>5g R&amp;R Classic Black Coffee</li><li>2oz hot water</li><li>2 tablespoons cinnamon syrup</li><li>Frothed milk</li><li>Cinnamon powder for sprinkle</li><li>Cinnamon stick for garnish</li></ul>
    <hr>
    <h3>INSTRUCTIONS:</h3>
    <ol><li><b>1.</b><span>Mix 2oz of hot water with one packet R&amp;R Classic Black Instant Coffee, mix well until powder is fully dissolved, and pour into a cup.</span></li><li><b>2.</b><span>Mix in the cinnamon syrup thoroughly.</span></li><li><b>3.</b><span>Top with frothed milk.</span></li><li><b>4.</b><span>Sprinkle with cinnamon powder.</span></li><li><b>5.</b><span>Garnish with a cinnamon stick.</span></li></ol>
  </div>
  <div class="logo"><span class="logo__dot"></span><span class="logo__name">RISE &amp;<br>ROAST</span></div>
</article>

<!-- Card 4 -->
<article class="card card--4">
  <svg class="card__art" viewBox="0 0 345 483">
    <path d="M345 300C315 305 310 345 330 370C345 395 325 440 310 483H345Z" fill="var(--mint)"/>
    <path d="M0 165C30 158 45 185 40 210C35 230 15 240 0 238Z" fill="var(--mint)"/>
    <path d="M60 0C45 40 52 140 95 200C140 260 240 285 345 284" fill="none" stroke="var(--mint)" stroke-width="6"/>
    <path role="img" aria-label="Photo of an espresso martini mocktail with foam and coffee beans, orange zest garnish" d="M68 0H345V280C250 281 150 258 102 198C62 145 55 60 68 0Z" fill="url(#g4)"/>
    <ellipse cx="36" cy="488" rx="104" ry="108" fill="none" stroke="var(--mint)" stroke-width="4"/>
    <ellipse cx="28" cy="488" rx="100" ry="106" fill="var(--white)"/>
    <defs><linearGradient id="g4" x1="0" y1="0" x2="1" y2="1"><stop offset="0" stop-color="#5a4636"/><stop offset=".5" stop-color="#8a7460"/><stop offset="1" stop-color="#3a3430"/></linearGradient></defs>
  </svg>
  <div class="title"><span style="left:167px;top:56px">Espresso</span><span style="left:131px;top:107px">Martini</span><span style="left:131px;top:161px">Mocktail</span></div>
  <p class="desc" style="left:20px;top:217px;width:98px">Invoke the spirit of the night with an Espresso Martini Mocktail. Vigorously shake a mixture of cold brew concentrate, simple syrup, and a tease of non-alcoholic coffee liqueur extract over ice. Once the concoction is chilled to perfection, perform a graceful strain into a martini glass and garnish with a trilogy of coffee beans or a curl of orange zest, a silent nod to the classic.</p>
  <div class="recipe" style="left:141px;top:283px">
    <h3>INGREDIENTS:</h3>
    <ul><li>5g R&amp;R Classic Black Coffee</li><li>2 oz hot water</li><li>1 oz simple syrup</li><li>1 oz non-alcoholic coffee liqueur extract</li><li>Ice cubes</li><li>Coffee beans for garnish</li></ul>
    <hr>
    <h3>INSTRUCTIONS:</h3>
    <ol style="width:195px"><li><b>1.</b><span>Mix 2oz of hot water with one packet R&amp;R Classic Black Instant Coffee, mix well until powder is fully dissolved.</span></li><li><b>2.</b><span>Fill a shaker with ice cubes.</span></li><li><b>2.</b><span>Add coffee, simple syrup, and coffee liqueur extract.</span></li><li><b>3.</b><span>Shake well until chilled.</span></li><li><b>4.</b><span>Strain into a martini glass.</span></li><li><b>5.</b><span>Garnish with coffee beans.</span></li></ol>
  </div>
  <div class="logo"><span class="logo__dot"></span><span class="logo__name">RISE &amp;<br>ROAST</span></div>
</article>

<!-- Card 5 -->
<article class="card card--5">
  <svg class="card__art" viewBox="0 0 345 483">
    <path d="M345 300C315 305 310 345 330 370C345 395 325 440 310 483H345Z" fill="var(--mint)"/>
    <path d="M0 285C25 275 45 300 38 325C32 345 15 352 0 350Z" fill="var(--mint)"/>
    <path d="M0 250C30 268 120 280 200 275C245 272 258 200 250 140" fill="none" stroke="var(--mint)" stroke-width="6"/>
    <path role="img" aria-label="Photo of a layered iced Irish cream coffee topped with whipped cream and chocolate drizzle" d="M0 0H225C258 45 252 190 234 240C220 272 140 270 70 262C30 258 10 250 0 242Z" fill="url(#g5)"/>
    <ellipse cx="36" cy="488" rx="104" ry="108" fill="none" stroke="var(--mint)" stroke-width="4"/>
    <ellipse cx="28" cy="488" rx="100" ry="106" fill="var(--white)"/>
    <defs><linearGradient id="g5" x1="0" y1="0" x2="1" y2="1"><stop offset="0" stop-color="#2a1c18"/><stop offset=".55" stop-color="#9a6c48"/><stop offset="1" stop-color="#1e1a18"/></linearGradient></defs>
  </svg>
  <div class="title"><span style="left:18px;top:140px">Irish Coffee</span><span style="left:18px;top:195px">Twist</span></div>
  <p class="desc" style="left:258px;top:22px;width:72px">Revel in the nostalgia of an Irish pub with our twist on the classic Irish Coffee. Blend the fulfilling body of brewed coffee with the smooth allure of non-alcoholic Irish cream syrup. Top the mixture with a dollop of whipped cream, and for the final flourish, a sprinkle of nutmeg or a single chocolate-covered espresso bean—a simple, yet eloquent homage to the original.</p>
  <div class="recipe" style="left:151px;top:303px">
    <h3>INGREDIENTS:</h3>
    <ul><li>5g R&amp;R Classic Black Coffee</li><li>8 oz hot water</li><li>2 tablespoons non-alcoholic Irish cream syrup</li><li>Whipped cream</li><li>Nutmeg sprinkle for garnish</li></ul>
    <hr>
    <h3>INSTRUCTIONS:</h3>
    <ol><li><b>1.</b><span>Mix 8oz of hot water with one packet R&amp;R Classic Black Instant Coffee, mix well until powder is fully dissolved.</span></li><li><b>2.</b><span>Mix coffee with Irish cream syrup.</span></li><li><b>2.</b><span>Top with whipped cream.</span></li><li><b>3.</b><span>Garnish with a sprinkle of nutmeg.</span></li></ol>
  </div>
  <div class="logo"><span class="logo__dot"></span><span class="logo__name">RISE &amp;<br>ROAST</span></div>
</article>

<!-- Card 6 -->
<article class="card card--6">
  <svg class="card__art" viewBox="0 0 345 483">
    <path d="M345 300C315 305 310 345 330 370C345 395 325 440 310 483H345Z" fill="var(--mint)"/>
    <path d="M0 168C60 162 100 200 140 238C175 268 240 272 300 248" fill="none" stroke="var(--mint)" stroke-width="6"/>
    <path role="img" aria-label="Photo of a layered Mexican coffee dessert in a footed glass with chocolate and cinnamon sticks" d="M0 0H318V195C300 240 255 258 205 252C130 245 90 165 0 160Z" fill="url(#g6)"/>
    <ellipse cx="36" cy="488" rx="104" ry="108" fill="none" stroke="var(--mint)" stroke-width="4"/>
    <ellipse cx="28" cy="488" rx="100" ry="106" fill="var(--white)"/>
    <defs><linearGradient id="g6" x1="0" y1="0" x2="1" y2="1"><stop offset="0" stop-color="#6a4a34"/><stop offset=".5" stop-color="#c8a888"/><stop offset="1" stop-color="#5a3a26"/></linearGradient></defs>
  </svg>
  <div class="title"><span style="left:19px;top:47px">Mexican</span><span style="left:19px;top:101px">Coffee Delight</span></div>
  <p class="desc" style="left:20px;top:217px;width:96px">Summon the vibrance of a festive evening with the Mexican Coffee Delight. In a clear mug, stir together spirited strong coffee with succulent chocolate syrup and a whisper of cinnamon. As you garnish with a twirl of whipped cream, add a cinnamon stick for authenticity, or be playful with a chocolate curl, embracing the rich heritage of Mexican flavors.</p>
  <div class="recipe" style="left:141px;top:294px">
    <h3>INGREDIENTS:</h3>
    <ul><li>5g R&amp;R Classic Black Coffee</li><li>8 oz hot water</li><li>2 tablespoons chocolate syrup</li><li>1/4 teaspoon cinnamon</li><li>Whipped cream</li><li>A cinnamon stick for garnish</li></ul>
    <hr>
    <h3>INSTRUCTIONS:</h3>
    <ol style="width:190px"><li><b>1.</b><span>Mix 8oz of hot water with one packet R&amp;R Classic Black Instant Coffee, mix well until powder is fully dissolved.</span></li><li><b>2.</b><span>Stir coffee with chocolate syrup and cinnamon.</span></li><li><b>3.</b><span>Pour into a fancy mug.</span></li><li><b>4.</b><span>Add whipped cream on top.</span></li><li><b>5.</b><span>Garnish with a cinnamon stick.</span></li></ol>
  </div>
  <div class="logo"><span class="logo__dot"></span><span class="logo__name">RISE &amp;<br>ROAST</span></div>
</article>

</body>
</html>
```